Redesign of Brightvale.com website

Our website was initially developed 6+ years ago and has been maintained by several different designers. As a result, it is overly complex, inconsistent format/layout and the content is not well structured/easy to navigate

We need the site redeveloped with a more modern look and feel, simpler content structure and ability to implement new/improved tools, such as: Dynamic Forms, Sales Funnels, Landing Pages, improved metadata of our pages and posts, improved SEO/Page ranking, etc.

We currently use SalesForce CRM, Constant Contact for marketing automation and SmartSheet forms. We are investigating Zapier for workflow integration which could extend to our website.

Our current website is developed in WordPress, ideally we will stick with this platform, but we’re happy to consider other CMS' if strongly recommended. We may decide to remove/consolidate some of the pages and/or content as part of this re-design.

We don't want to rebrand (ie change corporate logo, colours scheme etc) as part of this website redevelopment and it is critical that we don't lose our current Page Ranking, SEO rankings, backlink benefits, etc as part of this redevelopment.

Sites we like the feel/design of are: plorvista.com, quindlefax.com and tovalip.com

Target Market(s)

Corporate, Enterprise and Government B2B clients.

Coding

Coded - Design and coding required

Number of Pages Required

5+ page

Font styles to use
Sans Serif

Colors
ffffff
ec1f27

Requirements
Must have
• Must retain the majority of content on our existing website (although we may re-write some of it as part of this redesign process).
Nice to have
• See above "Project Description"
Should not have

```html
<!DOCTYPE html>
<html lang="en">
<head>
<meta charset="utf-8">
<title>Business Continuity Management – Brightvale</title>
<link href="https://fonts.googleapis.com/css2?family=Poppins:wght@300;400;500;600;700&display=swap" rel="stylesheet">
<style>
:root{
  --red:#ec1f27;
  --red-deep:#d11a22;
  --ink:#22242c;
  --text:#3a3d46;
  --muted:#7c7f88;
  --light:#f4f5f9;
  --line:#e3e5ea;
  --white:#ffffff;
  --footer:#262a35;
  --footer-text:#8b8f9a;
}
*{margin:0;padding:0;box-sizing:border-box}
html,body{width:1200px;height:4172px;overflow:hidden}
body{font-family:'Poppins',sans-serif;color:var(--text);background:var(--white);position:relative}
.abs{position:absolute}
section,header,footer{position:absolute;left:0;width:1200px}

/* header + hero */
.hero{top:0;height:465px;background:var(--light)}
.brand{display:flex;align-items:center;gap:8px;color:var(--red);font-weight:500;font-size:24px;letter-spacing:-.3px}
.brand-dot{width:16px;height:16px;border-radius:50%;background:var(--red)}
.hero .brand{left:162px;top:26px}
.main-nav{left:502px;top:36px;display:flex;gap:27px;font-size:13px;color:var(--ink)}
.btn-contact{left:941px;top:29px;width:96px;height:36px;background:var(--red);color:#fff;font-size:13px;font-weight:500;display:flex;align-items:center;justify-content:center;box-shadow:0 6px 14px rgba(236,31,39,.3)}
.hero-dot{left:100px;top:211px;width:35px;height:35px;border-radius:50%;background:#d6d8de}
.hero-title{left:173px;top:182px;font-size:51px;font-weight:600;line-height:58px;color:var(--ink);letter-spacing:-.5px}
.crumb-small{left:174px;top:367px;font-size:9px;color:var(--muted)}
.crumb{left:174px;top:386px;font-size:13px;color:var(--ink)}
.hero-art{left:660px;top:112px;width:404px;height:335px;border-radius:4px;background:radial-gradient(circle at 60% 45%,#f7c7c9 0%,#f3dcdd 40%,var(--light) 75%)}

/* intro */
.intro{top:465px;height:544px;background:var(--white)}
.intro-head{left:173px;top:56px;width:860px;font-size:36px;line-height:45px;color:var(--ink);font-weight:500}
.intro-head em{font-style:normal;color:var(--red);font-weight:600}
.intro-photo{left:217px;top:202px;width:403px;height:333px;background:linear-gradient(135deg,#1b3a57 0%,#2f6e8e 45%,#0f2236 100%);box-shadow:0 18px 40px rgba(0,0,0,.25)}
.intro-sub{left:671px;top:216px;width:300px;font-size:23px;line-height:29px;font-weight:600;color:var(--ink)}
.intro-copy{left:673px;top:332px;width:336px;font-size:12.5px;line-height:22px;color:var(--text)}
.intro-copy p+p{margin-top:10px}

/* ROI band */
.roi{top:1009px;height:454px;background:linear-gradient(100deg,#d92028 0%,#e8333a 55%,#d5232a 100%);overflow:hidden}
.roi-panel{left:163px;top:0;width:874px;height:60px;background:var(--white)}
.roi-rings{left:430px;top:60px;width:600px;height:300px;opacity:.18}
.roi-head{left:173px;top:120px;width:860px;font-size:34px;line-height:47px;color:#fff;font-weight:500}
.roi-head strong{font-weight:600}
.roi-copy{left:174px;top:240px;width:840px;font-size:12.5px;line-height:20px;color:#fff}
.roi-copy p{margin-bottom:16px}

/* services */
.services{top:1463px;height:850px;background:#fafafb}
.services-head{left:173px;top:80px;font-size:27px;line-height:36px;font-weight:600;color:var(--ink)}
.services-rule{left:440px;top:80px;width:1px;height:72px;background:var(--line)}
.services-intro{left:463px;top:96px;width:570px;font-size:12.5px;line-height:22px;color:var(--text)}
.service{width:300px;text-align:center}
.service svg{display:block;margin:0 auto}
.service h3{font-size:17px;font-weight:500;color:var(--ink);margin-top:22px}
.service p{font-size:12.5px;line-height:17px;color:var(--muted);margin:12px auto 0;width:200px}
.service.featured{background:#fff;box-shadow:0 12px 40px rgba(0,0,0,.08);width:300px;height:300px;padding-top:30px}

/* resources */
.resources{top:2313px;height:614px;background:var(--white)}
.res-title{left:188px;top:66px;font-size:31px;font-weight:500;color:var(--ink)}
.card{top:133px;width:264px;height:400px;background:#fff;box-shadow:0 8px 30px rgba(0,0,0,.1);padding:11px}
.card-img{width:242px;height:219px}
.card-date{font-size:10px;color:var(--muted);margin:20px 0 0 11px}
.card h4{font-size:13px;line-height:19px;font-weight:500;color:var(--ink);margin:8px 11px 0}
.card p{font-size:11px;line-height:17px;color:var(--muted);margin:8px 11px 0}
.card-meta{display:flex;justify-content:space-between;align-items:center;margin:26px 11px 0;font-size:10px;color:var(--muted)}
.card-meta b{font-weight:600;color:var(--ink);font-size:10px}
.views{display:flex;align-items:center;gap:6px}

/* cta */
.cta{top:2927px;height:229px;background:linear-gradient(90deg,#e2262d 0%,#ec3a40 55%,#e1242b 100%)}
.cta-title{left:220px;top:54px;font-size:41px;font-weight:600;color:#fff}
.cta-copy{left:220px;top:121px;width:560px;font-size:13px;line-height:24px;color:#fff}
.cta-copy strong{font-weight:600}
.cta-btn{left:797px;top:94px;width:182px;height:41px;background:#fff;color:var(--ink);font-size:13px;font-weight:500;display:flex;align-items:center;justify-content:center;gap:12px}

/* contact form */
.contact{top:3156px;height:602px;background:linear-gradient(180deg,#f6f7f9 0%,#eef0f3 100%)}
.contact-head{left:0;top:74px;width:1200px;text-align:center;font-size:27px;line-height:37px;font-weight:500;color:var(--ink)}
.contact-head em{font-style:normal;color:var(--red);font-weight:600}
.contact-sub{left:0;top:151px;width:1200px;text-align:center;font-size:12.5px;color:var(--ink)}
.field{height:41px;width:269px;background:#fff;border:1px solid var(--line);font-size:12px;color:var(--muted);padding:0 20px;display:flex;align-items:center;box-shadow:0 2px 6px rgba(0,0,0,.03)}
.field.active{background:var(--red);border-color:var(--red);color:#fff}
.field.area{width:851px;height:128px;align-items:flex-start;padding-top:14px}
.submit{left:513px;top:484px;width:174px;height:37px;background:var(--red);color:#fff;font-size:12px;font-weight:600;display:flex;align-items:center;justify-content:center}

/* footer */
.site-footer{top:3758px;height:414px;background:var(--footer)}
.site-footer .brand{left:175px;top:92px}
.foot-about{left:175px;top:152px;width:230px;font-size:11px;line-height:19px;color:#c4c7cf}
.socials{left:175px;top:250px;display:flex;gap:12px}
.socials span{width:32px;height:32px;border-radius:50%;background:#343946;display:flex;align-items:center;justify-content:center}
.socials span.on{background:var(--red)}
.socials i{width:6px;height:6px;border-radius:50%;background:#c4c7cf}
.socials span.on i{background:#fff}
.foot-col h5{font-size:13px;font-weight:600;color:#fff;margin-bottom:20px}
.foot-col a{display:block;font-size:11.5px;color:var(--footer-text);text-decoration:none;line-height:29px}
.foot-col a.current{color:#fff;text-decoration:underline}
.foot-rule{left:0;top:357px;width:1200px;height:1px;background:#343946}
.copyright{left:174px;top:381px;font-size:10.5px;color:var(--footer-text)}
.legal{left:866px;top:381px;font-size:10.5px;color:var(--footer-text)}
</style>
</head>
<body>

<section class="hero">
  <div class="abs brand"><span class="brand-dot"></span>brightvale</div>
  <nav class="abs main-nav"><span>Home</span><span>Services</span><span>About</span><span>Clients</span><span>Resources</span><span>Blog</span></nav>
  <div class="abs btn-contact">Contact</div>
  <div class="abs hero-dot"></div>
  <h1 class="abs hero-title">BusinessContinuity<br>Management</h1>
  <div class="abs crumb-small">SERVICES</div>
  <div class="abs crumb">BUSINESS CONTINUITY MANAGEMENT</div>
  <div class="abs hero-art" role="img" aria-label="Illustration of a plant growing from red money bags with coins and a rising arrow"></div>
</section>

<section class="intro">
  <h2 class="abs intro-head"><em>You need to be ready.</em> You can’t afford to play games with your business continuity.</h2>
  <div class="abs intro-photo" role="img" aria-label="Photo of a businessman touching a glowing financial chart interface"></div>
  <h3 class="abs intro-sub">Clear thinking, expert knowledge and a hands-on, practical approach</h3>
  <div class="abs intro-copy">
    <p>These elements are at the heart of sound business continuity management. They underpin the business impact analysis that is crucial to your enterprise. They guarantee the design of an effective business continuity plan.</p>
    <p>Trust Brightvale to provide you with the business continuity resources and expertise and the results you need.</p>
  </div>
</section>

<section class="roi">
  <svg class="abs roi-rings" viewBox="0 0 600 300" fill="none" stroke="#fff" stroke-width="3">
    <circle cx="80" cy="40" r="34"/><circle cx="290" cy="40" r="34"/><circle cx="500" cy="40" r="34"/>
    <circle cx="300" cy="240" r="120" stroke-width="1.5"/><circle cx="300" cy="240" r="80" stroke-width="1.5"/>
  </svg>
  <div class="abs roi-panel"></div>
  <h2 class="abs roi-head"><strong>Business Continuity Management</strong> Will Help Your Return on Investment</h2>
  <div class="abs roi-copy">
    <p>And that’s not all. We also work to identify additional opportunities for you. With Brightvale, your business continuity becomes an investment, not a cost.</p>
    <p>Besides giving you peace of mind, robust business continuity management leads to returns in positive synergies and cost reductions.</p>
    <p>Proven compliance becomes a competitive strength. Together, they can help your enterprise become more attractive to customers and more profitable.</p>
  </div>
</section>

<section class="services">
  <h2 class="abs services-head">Services to Fit Your<br>Needs, Precisely</h2>
  <div class="abs services-rule"></div>
  <p class="abs services-intro">Brightvale is always at the forefront of advances in methods, processes and technology. We provide practical business continuity assistance to the level you require.</p>

  <div class="abs service" style="left:122px;top:270px">
    <svg width="64" height="64" viewBox="0 0 64 64" fill="none" stroke="var(--red)" stroke-width="2"><path d="M32 52 L14 34 a10 10 0 0 1 18-12 a10 10 0 0 1 18 12 Z"/><path d="M10 36 h10 l4-8 l6 14 l4-6 h20"/><circle cx="46" cy="46" r="8"/><path d="M46 42 v8 M42 46 h8"/></svg>
    <h3>Health Check</h3>
    <p>Brings your business continuity in line with current best practices</p>
  </div>
  <div class="abs service featured" style="left:449px;top:210px">
    <svg width="100" height="100" viewBox="0 0 100 100"><circle cx="50" cy="50" r="50" fill="#74757a"/><path d="M64 30 C52 32 42 42 38 56 L44 62 C58 58 68 48 70 36 Z" fill="none" stroke="#fff" stroke-width="3"/><circle cx="57" cy="43" r="4" fill="none" stroke="#fff" stroke-width="3"/><path d="M38 56 L30 58 L36 48 M44 62 L42 70 L52 64 M34 66 L28 72" fill="none" stroke="#fff" stroke-width="3"/></svg>
    <h3>Quick Start</h3>
    <p>Fast, fixed price business continuity planning, ideal for small to medium enterprises</p>
  </div>
  <div class="abs service" style="left:777px;top:270px">
    <svg width="64" height="64" viewBox="0 0 64 64" fill="none" stroke="var(--red)" stroke-width="2"><rect x="20" y="6" width="24" height="12"/><circle cx="32" cy="28" r="6"/><path d="M20 46 c0-8 24-8 24 0"/><rect x="10" y="46" width="44" height="6"/><path d="M16 52 v8 M48 52 v8"/></svg>
    <h3>Consulting</h3>
    <p>For enterprises with unique needs in any part of the business continuity lifecycle</p>
  </div>

  <div class="abs service" style="left:122px;top:565px">
    <svg width="72" height="72" viewBox="0 0 72 72" fill="none" stroke="var(--red)" stroke-width="2"><rect x="6" y="10" width="46" height="36"/><path d="M12 40 v-10 M20 40 v-16 M28 40 v-8"/><path d="M34 30 l8-10 l8 4 l12-14"/><circle cx="52" cy="52" r="12"/><circle cx="52" cy="52" r="5"/></svg>
    <h3>Testing &amp; Exercising</h3>
    <p>To find and fix any flaws in existing business continuity plans</p>
  </div>
  <div class="abs service" style="left:449px;top:565px">
    <svg width="72" height="72" viewBox="0 0 72 72" fill="none" stroke="var(--red)" stroke-width="2"><rect x="8" y="6" width="28" height="18"/><rect x="36" y="14" width="28" height="18"/><circle cx="22" cy="38" r="6"/><circle cx="50" cy="44" r="6"/><path d="M10 62 c0-10 24-10 24 0 M38 66 c0-10 24-10 24 0"/></svg>
    <h3>Mentoring</h3>
    <p>Guidance and knowledge transfer from us to your business continuity managers</p>
  </div>
  <div class="abs service" style="left:777px;top:565px">
    <svg width="72" height="72" viewBox="0 0 72 72" fill="none" stroke="var(--red)" stroke-width="2"><circle cx="36" cy="18" r="10"/><circle cx="36" cy="18" r="4"/><path d="M36 30 v10 M22 50 l14-10 l14 10"/><circle cx="18" cy="54" r="6"/><circle cx="54" cy="54" r="6"/><path d="M8 40 v24 M64 40 v24"/></svg>
    <h3>Managed Service</h3>
    <p>A virtual business continuity manager for your BC plans, tests and training</p>
  </div>
</section>

<section class="resources">
  <h2 class="abs res-title">Related Resources</h2>
  <article class="abs card" style="left:173px">
    <div class="card-img" role="img" aria-label="Illustration of a laptop surrounded by blue technology icons" style="background:linear-gradient(135deg,#1b6fb8,#3aa3e0 60%,#0e4a86)"></div>
    <div class="card-date">11 February 2018</div>
    <h4>How’s Your User Experience for Your Disaster Recovery?</h4>
    <p>Lorem ipsum dolor sit amet, elit, sed consectetur adipiscing elit.</p>
    <div class="card-meta"><span class="views"><svg width="12" height="8" viewBox="0 0 12 8"><ellipse cx="6" cy="4" rx="5.5" ry="3.5" fill="none" stroke="#9aa" /><circle cx="6" cy="4" r="1.5" fill="#9aa"/></svg>783</span><b>READ MORE</b></div>
  </article>
  <article class="abs card" style="left:468px">
    <div class="card-img" role="img" aria-label="Photo of hands holding a smartphone with floating social icons" style="background:linear-gradient(135deg,#e8e4e0,#b79a85 60%,#7a5a48)"></div>
    <div class="card-date">11 February 2018</div>
    <h4>How’s Your User Experience for Your Disaster Recovery?</h4>
    <p>Lorem ipsum dolor sit amet, elit, sed consectetur adipiscing elit.</p>
    <div class="card-meta"><span class="views"><svg width="12" height="8" viewBox="0 0 12 8"><ellipse cx="6" cy="4" rx="5.5" ry="3.5" fill="none" stroke="#9aa" /><circle cx="6" cy="4" r="1.5" fill="#9aa"/></svg>783</span><b>READ MORE</b></div>
  </article>
  <article class="abs card" style="left:763px">
    <div class="card-img" role="img" aria-label="Photo of a phone on a dark surface with a connected world network" style="background:linear-gradient(135deg,#2a2c30,#4a4e55 55%,#16181b)"></div>
    <div class="card-date">11 February 2018</div>
    <h4>How’s Your User Experience for Your Disaster Recovery?</h4>
    <p>Lorem ipsum dolor sit amet, elit, sed consectetur adipiscing elit.</p>
    <div class="card-meta"><span class="views"><svg width="12" height="8" viewBox="0 0 12 8"><ellipse cx="6" cy="4" rx="5.5" ry="3.5" fill="none" stroke="#9aa" /><circle cx="6" cy="4" r="1.5" fill="#9aa"/></svg>783</span><b>READ MORE</b></div>
  </article>
</section>

<section class="cta" role="img" aria-label="Red tinted photo of a handshake behind the call to action">
  <h2 class="abs cta-title">Let us help you</h2>
  <p class="abs cta-copy"><strong>An initial discussion, free of charge.</strong> It could lead to you getting much more out of your business continuity management than you imagined.</p>
  <div class="abs cta-btn">Contact Us Today <svg width="8" height="12" viewBox="0 0 8 12"><path d="M1 1 L6 6 L1 11" fill="none" stroke="var(--ink)" stroke-width="1.8"/></svg></div>
</section>

<section class="contact">
  <h2 class="abs contact-head"><em>Contact Us Now</em> For A Confidential Business<br>Continuity Assessment.</h2>
  <p class="abs contact-sub">Just add your details in the the form below and one of our expert consultants will contact you.</p>
  <div class="abs field" style="left:173px;top:205px">Your Name</div>
  <div class="abs field active" style="left:465px;top:205px">Email</div>
  <div class="abs field" style="left:755px;top:205px">Phone</div>
  <div class="abs field" style="left:173px;top:265px">Select A Service</div>
  <div class="abs field" style="left:465px;top:265px">Preferred Contact Time</div>
  <div class="abs field" style="left:755px;top:265px">Company/Business Name*</div>
  <div class="abs field area" style="left:173px;top:325px">Any Additional Information</div>
  <div class="abs submit">SUBMIT NOW</div>
</section>

<footer class="site-footer">
  <div class="abs brand"><span class="brand-dot"></span>brightvale</div>
  <p class="abs foot-about">Why I say old chap that is spiffing bodge, blag pardon me buggered mufty Oxford butty bubble and squeak wind up, brown bread the full monty bloke!</p>
  <div class="abs socials"><span><i></i></span><span class="on"><i></i></span><span><i></i></span><span><i></i></span></div>
  <div class="abs foot-col" style="left:515px;top:93px"><h5>Company</h5><a>Home</a><a>Services</a><a class="current">About Us</a><a>Clients</a><a>Resources</a><a>Blog</a></div>
  <div class="abs foot-col" style="left:682px;top:93px"><h5>Our Solutions</h5><a>Resilience &amp; Continuity</a><a>Security Management</a><a>IT Services &amp; Solutions</a><a>Data Management</a><a>Software Solutions</a><a>More</a></div>
  <div class="abs foot-col" style="left:901px;top:93px"><h5>Team Solutions</h5><a>Meet The Team</a><a>Partners</a><a>Faq</a><a>Testimonials</a><a>Sitemap</a><a>See All Teams</a></div>
  <div class="abs foot-rule"></div>
  <div class="abs copyright">Copyright © 2021 Brightvale</div>
  <div class="abs legal">Terms of Use &nbsp;&nbsp; | &nbsp;&nbsp; Privacy Policy</div>
</footer>

</body>
</html>
```